Washbag retail Packaging

We need a cardboard insert card design for a delicates washbag. The size for front panel would be 9cm wide and height 12cm, then a fold and the back panel would be the same size. This insert is packed into a clear hangsell polybag , and the white mesh washbag is folded up inside. We want to extend our brand using similar fonts , and colours - as shown in the photgraph, the PMS 241 is really our brand colour. But also introduce something appealing a beautiful about the washbag packaging. The washbag itself is a very plain and boring product. I have included an old artwork for the same product - the yellow box which does not suit the range at all. Please note the new packaging is not a box, but an insert card in a poly bag, and there will not be a window.
Updates

Project Deadline Extended Reason: We have extended the deadline to allow more designers to participate and as its our first time using the service. Added Thursday, January 12, 2017

Target Market(s)

Mainly women all ages, Mid range supermarket, lingerie stores, hosiery and stockings stores

Industry/Entity Type

Retail

Font styles to use
Sans Serif

Colors
e667a6
faeaf3
eea4c8
b868aa

Requirements
Must have
• PMS 241 and work with other products in the range
Nice to have
• Something a little more pretty

```html
<!DOCTYPE html>
<html lang="en">
<head>
<meta charset="utf-8">
<title>Bellmere Wash Bag – Insert Card, Front and Back Panels</title>
<link rel="stylesheet" href="https://fonts.googleapis.com/css2?family=Ubuntu:wght@400;500;700&display=swap">
<style>
  :root {
    --stage: #f1efec;
    --pink-light: #eea4c8;
    --pink-mid: #e667a6;
    --pink-brand: #d6248c;
    --magenta-deep: #a80a6e;
    --magenta-dark: #8c0059;
    --blush: #faeaf3;
    --mauve: #b868aa;
    --ink: #2a0a1c;
    --white: #ffffff;
    --mesh: #ece9e4;
    --fold: rgba(120, 0, 70, 0.35);
  }
  * { margin: 0; padding: 0; box-sizing: border-box; }
  html, body { width: 1200px; height: 1000px; overflow: hidden; }
  body {
    background: var(--stage);
    font-family: "Ubuntu", sans-serif;
    position: relative;
  }
  .insert-card {
    position: absolute;
    left: 180px; top: 220px;
    width: 840px; height: 560px;
    display: flex;
    box-shadow: 0 6px 24px rgba(90, 0, 50, 0.18);
  }
  .card-panel {
    position: relative;
    width: 420px; height: 560px;
    overflow: hidden;
  }
  .card-panel + .card-panel { border-left: 1px dashed var(--fold); }
  .panel-art { position: absolute; inset: 0; width: 420px; height: 560px; }
  .bubble-area {
    position: absolute; left: 0; top: 0; width: 420px; height: 240px;
    background:
      radial-gradient(circle at 12% 62%, rgba(255,255,255,0.24) 0 30px, transparent 32px),
      radial-gradient(circle at 88% 40%, rgba(255,255,255,0.22) 0 24px, transparent 26px),
      radial-gradient(circle at 80% 78%, rgba(255,255,255,0.18) 0 16px, transparent 18px);
  }
  .flower-area {
    position: absolute; left: 0; top: 330px; width: 420px; height: 230px;
    background: radial-gradient(ellipse at 50% 60%, rgba(238,164,200,0.45) 0%, rgba(238,164,200,0.18) 60%, rgba(238,164,200,0) 100%);
  }
  .brand {
    position: absolute; top: 34px; left: 0; width: 420px;
    display: flex; justify-content: center; align-items: center; gap: 9px;
  }
  .brand-dot { width: 16px; height: 16px; border-radius: 50%; background: var(--magenta-deep); }
  .brand-name { font-weight: 500; font-size: 32px; color: var(--magenta-deep); }
  .product-title {
    position: absolute; top: 100px; left: 0; width: 420px;
    text-align: center;
    font-weight: 700; font-size: 80px; line-height: 1;
    color: var(--magenta-deep);
    letter-spacing: -1px;
    text-shadow:
      3px 0 0 var(--white), -3px 0 0 var(--white), 0 3px 0 var(--white), 0 -3px 0 var(--white),
      2px 2px 0 var(--white), -2px 2px 0 var(--white), 2px -2px 0 var(--white), -2px -2px 0 var(--white),
      4px 5px 6px rgba(80, 0, 40, 0.35);
  }
  .tagline {
    position: absolute; top: 234px; left: 0; width: 420px;
    text-align: center; font-size: 12.5px; color: var(--ink);
  }
  .product-view {
    position: absolute; left: 70px; top: 268px;
    width: 280px; height: 210px;
    border-radius: 16px;
    border: 4px solid var(--blush);
    background: radial-gradient(ellipse at center, #f8f6f3 0%, var(--mesh) 70%, #dcd8d2 100%);
    box-shadow: 0 4px 10px rgba(80, 0, 40, 0.25);
  }
  .care-line {
    position: absolute; top: 508px; left: 0; width: 420px;
    text-align: center; font-size: 13px; color: var(--blush);
  }
</style>
</head>
<body>
  <main class="insert-card">
    <section class="card-panel panel-front" aria-label="Front panel">
      <svg class="panel-art" viewBox="0 0 420 560" aria-hidden="true">
        <rect width="420" height="560" fill="#e862a8"/>
        <path d="M0 330 C 110 265, 230 230, 420 210 L420 560 L0 560 Z" fill="#d93a98"/>
        <path d="M0 395 C 115 330, 250 295, 420 280 L420 560 L0 560 Z" fill="#c8168a"/>
        <path d="M0 495 C 140 488, 280 484, 420 476 L420 560 L0 560 Z" fill="#a80a6e"/>
      </svg>
      <div class="bubble-area" role="img" aria-label="Soft translucent soap bubbles floating across the upper pink area"></div>
      <div class="flower-area" role="img" aria-label="Scattered small pale pink daisy flowers over the magenta waves"></div>
      <div class="brand"><span class="brand-dot"></span><span class="brand-name">bellmere</span></div>
      <h1 class="product-title">Wash Bag</h1>
      <p class="tagline">protects small and delilicate items from tangles and snags</p>
      <div class="product-view" role="img" aria-label="Printed close-up photo of the white mesh washbag"></div>
      <p class="care-line">cares for hosiery, underwear, socks, baby clothes</p>
    </section>

    <section class="card-panel panel-back" aria-label="Back panel">
      <svg class="panel-art" viewBox="0 0 420 560" aria-hidden="true">
        <rect width="420" height="560" fill="#e862a8"/>
        <path d="M0 330 C 110 265, 230 230, 420 210 L420 560 L0 560 Z" fill="#d93a98"/>
        <path d="M0 395 C 115 330, 250 295, 420 280 L420 560 L0 560 Z" fill="#c8168a"/>
        <path d="M0 495 C 140 488, 280 484, 420 476 L420 560 L0 560 Z" fill="#a80a6e"/>
      </svg>
      <div class="bubble-area" role="img" aria-label="Soft translucent soap bubbles floating across the upper pink area"></div>
      <div class="flower-area" role="img" aria-label="Scattered small pale pink daisy flowers over the magenta waves"></div>
      <div class="brand"><span class="brand-dot"></span><span class="brand-name">bellmere</span></div>
      <h2 class="product-title">Wash Bag</h2>
      <p class="tagline">protects small and delilicate items from tangles and snags</p>
      <div class="product-view" role="img" aria-label="Printed close-up photo of the white mesh washbag"></div>
      <p class="care-line">cares for hosiery, underwear, socks, baby clothes</p>
    </section>
  </main>
</body>
</html>
```